Word Cloud for Cocktail Napkins

We are needing the following list of words put together in a word cloud (like the attached example)
Intercourse
Moist
Crampon
Sack
Crusty
Crevice
Cartilage
Squirt
Unicorn
Rainbows
Self tanner
Goiter
Clowns
Dessicate
Lettuce
Rubber
Pus
This is a funny joke for our friends so we are wanting this to be fun!
Thank you!

```html
<!DOCTYPE html>
<html lang="en">
<head>
<meta charset="utf-8">
<title>Word Cloud — Cocktail Napkins</title>
<link rel="stylesheet" href="https://fonts.googleapis.com/css2?family=Chewy&display=swap">
<style>
  :root {
    --bg-center: #fffdf7;
    --bg-edge: #ffe9f2;
    --shadow: rgba(40, 30, 60, 0.18);
    --c-slate: #5c6b78;
    --c-sun: #f5b800;
    --c-magenta: #e0147a;
    --c-ocean: #1487c9;
    --c-crimson: #d81f4a;
    --c-lavender: #8a6cc4;
    --c-green: #17a05a;
    --c-orange: #f07b16;
    --c-red: #e23a2b;
    --c-sky: #1aa9df;
    --c-navy: #3a2f8c;
    --c-rose: #ee8fa6;
    --c-plum: #a0308f;
    --c-teal: #1aa39a;
    --c-lime: #7cb82f;
    --c-grape: #6a3f90;
  }
  html, body {
    margin: 0;
    width: 1200px;
    height: 1200px;
    overflow: hidden;
  }
  .canvas {
    width: 1200px;
    height: 1200px;
    background: radial-gradient(ellipse at center, var(--bg-center) 50%, var(--bg-edge) 100%);
  }
  .word-cloud { display: block; }
  .word {
    font-family: "Chewy", "Comic Sans MS", cursive;
    filter: drop-shadow(3px 3px 0 var(--shadow));
  }
  .slate { fill: var(--c-slate); }
  .sun { fill: var(--c-sun); }
  .magenta { fill: var(--c-magenta); }
  .ocean { fill: var(--c-ocean); }
  .crimson { fill: var(--c-crimson); }
  .lavender { fill: var(--c-lavender); }
  .green { fill: var(--c-green); }
  .orange { fill: var(--c-orange); }
  .red { fill: var(--c-red); }
  .sky { fill: var(--c-sky); }
  .navy { fill: var(--c-navy); }
  .rose { fill: var(--c-rose); }
  .plum { fill: var(--c-plum); }
  .teal { fill: var(--c-teal); }
  .lime { fill: var(--c-lime); }
  .grape { fill: var(--c-grape); }
</style>
</head>
<body>
<main class="canvas">
  <svg class="word-cloud" width="1200" height="1200" viewBox="0 0 1200 1200" aria-label="Word cloud">
    <text class="word slate" x="300" y="330" font-size="90" textLength="290" lengthAdjust="spacingAndGlyphs">Crampon</text>
    <text class="word lavender" x="630" y="330" font-size="90" textLength="290" lengthAdjust="spacingAndGlyphs">Unicorn</text>

    <text class="word magenta" x="150" y="435" font-size="100" textLength="320" lengthAdjust="spacingAndGlyphs">Crevice</text>
    <text class="word teal" x="505" y="440" font-size="120" textLength="160" lengthAdjust="spacingAndGlyphs">Pus</text>
    <text class="word orange" x="700" y="435" font-size="100" textLength="330" lengthAdjust="spacingAndGlyphs">Rubber</text>

    <text class="word red" x="110" y="535" font-size="88" textLength="410" lengthAdjust="spacingAndGlyphs">Self tanner</text>
    <text class="word rose" x="555" y="535" font-size="94" textLength="260" lengthAdjust="spacingAndGlyphs">Goiter</text>
    <text class="word green" x="850" y="535" font-size="88" textLength="240" lengthAdjust="spacingAndGlyphs">Squirt</text>

    <text class="word sky" x="100" y="650" font-size="120" textLength="590" lengthAdjust="spacingAndGlyphs">Intercourse</text>
    <text class="word sun" x="730" y="650" font-size="120" textLength="360" lengthAdjust="spacingAndGlyphs">Moist</text>

    <text class="word plum" x="110" y="760" font-size="96" textLength="310" lengthAdjust="spacingAndGlyphs">Clowns</text>
    <text class="word navy" x="455" y="760" font-size="104" textLength="400" lengthAdjust="spacingAndGlyphs">Rainbows</text>
    <text class="word crimson" x="890" y="760" font-size="104" textLength="200" lengthAdjust="spacingAndGlyphs">Sack</text>

    <text class="word ocean" x="170" y="865" font-size="96" textLength="410" lengthAdjust="spacingAndGlyphs">Cartilage</text>
    <text class="word lime" x="620" y="865" font-size="96" textLength="330" lengthAdjust="spacingAndGlyphs">Lettuce</text>

    <text class="word grape" x="260" y="965" font-size="90" textLength="290" lengthAdjust="spacingAndGlyphs">Crusty</text>
    <text class="word slate" x="590" y="965" font-size="84" textLength="370" lengthAdjust="spacingAndGlyphs">Dessicate</text>
  </svg>
</main>
</body>
</html>
```